Marlowe Lane Quilts

We are opening a long-arm quilting business where customers will bring in their pieced quilt top and have us quilt it to the batting and backing. We own a Brevant Orlix Framer - photos can be found on the internet. We would like for our business card and logo to include an image of a long arm quilting machine so that our business type would be easily recognizable. We like lots of color and contemporary styling, perhaps with colorful fabric flowing on the card as well. It needs to be something transferable to a store window and/or to a decal for our car to aid in advertising.

Industry/Entity Type

Store

Colors
fff5ee
fde8d3

```html
<!DOCTYPE html>
<html lang="en">
<head>
<meta charset="utf-8">
<title>Marlowe Lane Quilts – Business Card</title>
<link href="https://fonts.googleapis.com/css2?family=Chewy&family=Arimo:wght@400&display=swap" rel="stylesheet">
<style>
  :root {
    --page-bg: #d9d9d9;
    --card-bg: #0b0b0b;
    --brand-yellow: #ffe600;
    --text-white: #ffffff;
    --swirl-orange: #ff8a00;
    --swirl-purple: #8a2fc9;
    --swirl-magenta: #d0309a;
    --swirl-green: #1e8a4a;
    --swirl-blue: #2446b8;
    --machine-gold: #c9a91a;
  }
  html, body {
    margin: 0;
    padding: 0;
    width: 1200px;
    height: 900px;
    overflow: hidden;
    background: var(--page-bg);
  }
  .business-card {
    position: absolute;
    left: 80px;
    top: 153px;
    width: 1040px;
    height: 594px;
    border-radius: 44px;
    background: var(--card-bg);
    overflow: hidden;
    font-family: "Arimo", Arial, sans-serif;
    color: var(--text-white);
  }
  .fabric-swirls {
    position: absolute;
    inset: 0;
    background:
      radial-gradient(ellipse 260px 300px at 90px 330px, rgba(255,138,0,0.55), transparent 70%),
      radial-gradient(ellipse 200px 180px at 250px 60px, rgba(30,138,74,0.45), transparent 70%),
      radial-gradient(ellipse 260px 260px at 880px 120px, rgba(208,48,154,0.45), transparent 70%),
      radial-gradient(ellipse 300px 260px at 930px 470px, rgba(138,47,201,0.55), transparent 70%),
      radial-gradient(ellipse 240px 200px at 560px 340px, rgba(36,70,184,0.4), transparent 70%),
      radial-gradient(ellipse 200px 160px at 420px 560px, rgba(208,48,154,0.35), transparent 70%);
  }
  .owners {
    position: absolute;
    right: 40px;
    top: 28px;
    text-align: right;
  }
  .owners-names {
    color: var(--brand-yellow);
    font-size: 28px;
    line-height: 1.2;
  }
  .owners-title {
    font-size: 24px;
    line-height: 1.3;
  }
  .machine-illustration {
    position: absolute;
    left: 310px;
    top: 100px;
    width: 320px;
    height: 180px;
    border-radius: 6px;
    background: linear-gradient(180deg, #f3d23a 0%, var(--machine-gold) 60%, #7a6410 100%);
  }
  .brand-name {
    position: absolute;
    left: 0;
    right: 0;
    top: 272px;
    margin: 0;
    padding-left: 70px;
    text-align: center;
    font-family: "Chewy", cursive;
    font-weight: 400;
    font-size: 76px;
    color: var(--brand-yellow);
    line-height: 1;
  }
  .contact-list {
    position: absolute;
    left: 40px;
    top: 408px;
    margin: 0;
    padding: 0;
    list-style: none;
    font-size: 33px;
    line-height: 40px;
  }
  .contact-item {
    display: flex;
    align-items: center;
    gap: 10px;
  }
  .contact-icon {
    width: 34px;
    height: 34px;
    flex: none;
  }
</style>
</head>
<body>
  <section class="business-card">
    <div class="fabric-swirls" role="img" aria-label="Colourful flowing fabric swirls in orange, green, blue, magenta and purple on a dark damask background"></div>

    <div class="owners">
      <div class="owners-names">Dorian Vale &amp; Nessa Holloway</div>
      <div class="owners-title">Owners</div>
    </div>

    <div class="machine-illustration" role="img" aria-label="Illustration of a Brevant Orlix Framer long-arm quilting machine on its frame, in gold tones"></div>

    <h1 class="brand-name">Marlowe Lane Quilts</h1>

    <ul class="contact-list">
      <li class="contact-item">
        <svg class="contact-icon" viewBox="0 0 24 24" aria-hidden="true"><path fill="#fff" d="M6.6 10.8a15 15 0 0 0 6.6 6.6l2.2-2.2c.3-.3.7-.4 1-.2 1.1.4 2.3.6 3.6.6.6 0 1 .4 1 1V20c0 .6-.4 1-1 1A17 17 0 0 1 3 4c0-.6.4-1 1-1h3.5c.6 0 1 .4 1 1 0 1.3.2 2.5.6 3.6.1.3 0 .7-.2 1z"/></svg>
        <span>707.555.0148</span>
      </li>
      <li class="contact-item">
        <svg class="contact-icon" viewBox="0 0 24 24" aria-hidden="true"><g fill="none" stroke="#fff" stroke-width="1.8"><circle cx="12" cy="12" r="9.5"/><ellipse cx="12" cy="12" rx="4" ry="9.5"/><path d="M2.5 12h19M4 7h16M4 17h16"/></g></svg>
        <span>www.marlowelanequilts.com</span>
      </li>
      <li class="contact-item">
        <svg class="contact-icon" viewBox="0 0 24 24" aria-hidden="true"><rect x="2" y="5" width="20" height="14" rx="1.5" fill="#fff"/><path d="M2.5 6l9.5 7 9.5-7" fill="none" stroke="#0b0b0b" stroke-width="1.6"/></svg>
        <span>marlowelanequilts@inbox.com</span>
      </li>
      <li class="contact-item">
        <svg class="contact-icon" viewBox="0 0 24 24" aria-hidden="true"><path fill="#fff" d="M12 2.5 1.5 12H5v9h5.5v-6h3v6H19v-9h3.5z"/></svg>
        <span>418 Harbor Street, Corliss, CA 94590</span>
      </li>
    </ul>
  </section>
</body>
</html>
```